Business Card desgin, company called Stand Fast.

I am looking for the logo colors (3) to be used on the card in whatever design you think might work. the certifications are on the back (4) on the front will be my name, Dana Whitlock, owner/instructor, phone 208.555.0193, website www.sfx-drills.example, email dw@sfx-drills.example. im flexible on fonts.

Target Market(s)

firearms owners

Industry/Entity Type

firearms training

Contact Information for Business Card

certification icons on back

```html
<!DOCTYPE html>
<html lang="en">
<head>
<meta charset="utf-8">
<title>Stand Fast — Business Card</title>
<link rel="stylesheet" href="https://fonts.googleapis.com/css2?family=Lato:wght@300;400;700&family=Montserrat:wght@800&family=Lora:wght@700&display=swap">
<style>
  :root {
    --stage: #141518;
    --navy-light: #1f3a5a;
    --navy-dark: #0f2238;
    --red: #d7262e;
    --white: #f2f4f7;
    --badge-light: #e4e7eb;
    --badge-orange: #d9772a;
    --badge-dark: #34373d;
  }
  * { margin: 0; padding: 0; box-sizing: border-box; }
  html, body { width: 1200px; height: 963px; overflow: hidden; }
  body {
    background: var(--stage);
    display: flex;
    flex-direction: column;
    align-items: center;
    justify-content: center;
    gap: 56px;
    font-family: "Lato", sans-serif;
  }
  .card {
    position: relative;
    width: 630px;
    height: 360px;
    border-radius: 22px;
    background: linear-gradient(135deg, var(--navy-light) 0%, var(--navy-dark) 100%);
    box-shadow: 0 14px 40px rgba(0,0,0,.55);
    overflow: hidden;
    color: var(--white);
  }

  /* Front */
  .brand {
    position: absolute;
    left: 60px;
    top: 46px;
    display: flex;
    align-items: center;
    gap: 16px;
  }
  .brand-dot {
    width: 44px; height: 44px;
    border-radius: 50%;
    background: var(--red);
  }
  .brand-name {
    font-family: "Montserrat", sans-serif;
    font-weight: 800;
    font-size: 34px;
    letter-spacing: 1px;
    color: var(--red);
    text-transform: uppercase;
  }
  .brand-url {
    position: absolute;
    left: 120px;
    top: 100px;
    font-family: "Lora", serif;
    font-weight: 700;
    font-size: 17px;
    letter-spacing: .5px;
  }
  .person {
    position: absolute;
    left: 60px;
    top: 158px;
  }
  .person-name {
    font-size: 28px;
    font-weight: 400;
    color: var(--red);
    line-height: 1.1;
  }
  .person-role {
    font-size: 16px;
    font-weight: 400;
    margin-top: 4px;
  }
  .contact-list {
    list-style: none;
    margin-top: 16px;
    font-size: 16px;
    line-height: 1.75;
  }
  .contact-list li { display: flex; align-items: center; gap: 12px; }
  .contact-list li.plain { padding-left: 28px; }
  .contact-icon { width: 16px; height: 16px; fill: var(--red); flex: none; }

  /* Back */
  .cert-title {
    position: absolute;
    right: 56px;
    top: 46px;
    font-size: 44px;
    font-weight: 300;
    letter-spacing: 1px;
  }
  .cert-badges {
    position: absolute;
    left: 60px;
    top: 135px;
    width: 510px;
    height: 190px;
  }
</style>
</head>
<body>

  <section class="card card-front" aria-label="Card front">
    <div class="brand">
      <span class="brand-dot"></span>
      <span class="brand-name">Stand Fast</span>
    </div>
    <div class="brand-url">WWW.SFX-Drills.example</div>

    <div class="person">
      <div class="person-name">Dana Whitlock</div>
      <div class="person-role">owner/instructor</div>
      <ul class="contact-list">
        <li>
          <svg class="contact-icon" viewBox="0 0 24 24" aria-hidden="true"><path d="M6.6 10.8a15.1 15.1 0 0 0 6.6 6.6l2.2-2.2a1 1 0 0 1 1-.25 11.4 11.4 0 0 0 3.6.57 1 1 0 0 1 1 1V20a1 1 0 0 1-1 1A17 17 0 0 1 3 4a1 1 0 0 1 1-1h3.5a1 1 0 0 1 1 1c0 1.25.2 2.45.57 3.6a1 1 0 0 1-.25 1z"/></svg>
          208.555.0193
        </li>
        <li>
          <svg class="contact-icon" viewBox="0 0 24 24" aria-hidden="true"><path d="M2 5h20v14H2z M2 5l10 8 10-8" stroke="#0f2238" stroke-width="1.5"/></svg>
          dw@sfx-drills.example
        </li>
        <li>
          <svg class="contact-icon" viewBox="0 0 24 24" aria-hidden="true"><circle cx="12" cy="12" r="10"/><path d="M2 12h20M12 2c3 3 3 17 0 20M12 2c-3 3-3 17 0 20" stroke="#0f2238" stroke-width="1.5" fill="none"/></svg>
          www.sfx-drills.example
        </li>
        <li class="plain">www.sfx-drills.example</li>
      </ul>
    </div>
  </section>

  <section class="card card-back" aria-label="Card back">
    <h2 class="cert-title">Certifications</h2>
    <svg class="cert-badges" viewBox="0 0 510 190" role="img" aria-label="Four certification badges">
      <rect x="0" y="0" width="105" height="95" rx="10" fill="var(--badge-light)"/>
      <rect x="130" y="30" width="105" height="95" rx="10" fill="var(--badge-orange)"/>
      <rect x="265" y="62" width="105" height="95" rx="10" fill="var(--badge-dark)"/>
      <rect x="400" y="92" width="105" height="95" rx="10" fill="var(--badge-dark)"/>
    </svg>
  </section>

</body>
</html>
```